Stationary Design Letterhead and Envelope

Artist should provide Letterhead and envelop stationary designs

Info for stationary:
Fenwarde Outdoor Advertising
4857 Mesa Rd. 318 N. PO BOX 582917
Austin, TX 78651

Dale Fenwarde
President
512-608-2917
dale@fenwardeoutdoor.example
fenwardeoutdoor.example

Target Market(s)

clients

Colors
0054AA
0677BA
7BADD7
CADEEF
E8F1F8

Requirements
Must have
• high quality unique eye catching and dynamic

```html
<!DOCTYPE html>
<html lang="en">
<head>
<meta charset="utf-8">
<title>Fenwarde Outdoor Advertising – Stationery</title>
<link href="https://fonts.googleapis.com/css2?family=Open+Sans:ital,wght@0,400;0,700;1,400&display=swap" rel="stylesheet">
<style>
  :root{
    --backdrop:#C2B39A;
    --paper:#FFFFFF;
    --brand-blue:#0071AE;
    --footer-blue:#0487C0;
    --wedge-blue:#1F8BB3;
    --swoosh-black:#050505;
    --swoosh-gray:#D6D6D6;
    --ink:#222222;
  }
  *{box-sizing:border-box;margin:0;padding:0}
  html,body{width:1200px;height:819px;overflow:hidden}
  body{background:var(--backdrop);font-family:"Open Sans",Arial,sans-serif;position:relative}
  .sheet{position:absolute;background:var(--paper);box-shadow:2px 3px 8px rgba(0,0,0,.28);overflow:hidden}
  .swoosh{position:absolute;left:0;bottom:0;display:block}

  .wordmark{font-family:"Open Sans",Arial,sans-serif;font-weight:700;color:var(--brand-blue);line-height:1;position:absolute}
  .wordmark .name{display:block;letter-spacing:.5px}
  .wordmark .tag{display:block;letter-spacing:.2px}
  .wordmark.on-blue{color:var(--paper);text-align:center}

  /* Letterhead */
  .letterhead{left:84px;top:59px;width:484px;height:692px}
  .letterhead .wordmark{left:33px;top:23px}
  .letterhead .wordmark .name{font-size:22px}
  .letterhead .wordmark .tag{font-size:8.2px;margin-top:3px}
  .letterhead-footer{position:absolute;left:0;top:645px;width:484px;height:30px;color:var(--paper);font-size:6.6px;line-height:1.05}
  .contact{position:absolute;display:flex;align-items:flex-start;gap:3px}
  .contact svg{flex:none;width:7px;height:7px;fill:currentColor}
  .letterhead-footer .phone{left:22px;top:6px}
  .letterhead-footer .mail{left:105px;top:5px}
  .letterhead-footer .web{left:235px;top:5px}
  .letterhead-footer .addr{left:336px;top:2px}

  /* Envelope */
  .envelope{left:654px;top:61px;width:505px;height:307px;background:none;box-shadow:none;overflow:visible}
  .envelope .flap{position:absolute;left:0;top:0;display:block}
  .envelope-body{position:absolute;left:0;top:55px;width:505px;height:252px;background:var(--paper);overflow:hidden;box-shadow:2px 3px 8px rgba(0,0,0,.28)}
  .envelope .wordmark{left:50%;top:10px;transform:translateX(-50%) rotate(180deg)}
  .envelope .wordmark .name{font-size:17px}
  .envelope .wordmark .tag{font-size:6.4px;margin-top:2px}

  /* Business cards */
  .card-back{left:778px;top:418px;width:239px;height:141px;background:var(--brand-blue)}
  .card-back .wordmark{left:0;right:0;top:55px}
  .card-back .wordmark .name{font-size:17px}
  .card-back .wordmark .tag{font-size:6.5px;margin-top:3px}

  .card-front{left:777px;top:601px;width:239px;height:140px;color:var(--ink)}
  .card-front .wordmark{left:11px;top:16px}
  .card-front .wordmark .name{font-size:12px}
  .card-front .wordmark .tag{font-size:4.6px;margin-top:2px}
  .person{position:absolute;left:12px;top:59px;line-height:1.2}
  .person-name{font-size:8px;color:var(--brand-blue)}
  .person-role{font-size:7.4px;font-style:italic}
  .card-contacts{position:absolute;left:12px;top:89px;font-size:6.4px;line-height:1.05}
  .card-contacts .contact{position:static;margin-bottom:2.6px}
  .card-contacts .contact svg{fill:var(--brand-blue)}
</style>
</head>
<body>

<svg width="0" height="0" style="position:absolute">
  <defs>
    <symbol id="icon-phone" viewBox="0 0 24 24"><path d="M6.6 10.8a15.1 15.1 0 0 0 6.6 6.6l2.2-2.2c.3-.3.7-.4 1-.2 1.1.4 2.3.6 3.6.6.6 0 1 .4 1 1V20c0 .6-.4 1-1 1A17 17 0 0 1 3 4c0-.6.4-1 1-1h3.5c.6 0 1 .4 1 1 0 1.3.2 2.5.6 3.6.1.3 0 .7-.2 1z"/></symbol>
    <symbol id="icon-mail" viewBox="0 0 24 24"><path d="M2 5h20v14H2z M3.5 6.5 12 13l8.5-6.5" fill="currentColor"/><path d="M3 6l9 7 9-7M3 18l7-6M21 18l-7-6" stroke="#fff" stroke-width="1.6" fill="none"/></symbol>
    <symbol id="icon-globe" viewBox="0 0 24 24"><path d="M12 2a10 10 0 1 0 0 20 10 10 0 0 0 0-20zm0 2c1.2 0 2.5 2.3 2.9 6H9.1C9.5 6.3 10.8 4 12 4zM4.1 10h3c.1-2.2.5-4.1 1.2-5.3A8 8 0 0 0 4.1 10zm0 4a8 8 0 0 0 4.2 5.3c-.7-1.2-1.1-3.1-1.2-5.3zm5 0c.4 3.7 1.7 6 2.9 6s2.5-2.3 2.9-6zm7.8 0c-.1 2.2-.5 4.1-1.2 5.3a8 8 0 0 0 4.2-5.3zm3-4a8 8 0 0 0-4.2-5.3c.7 1.2 1.1 3.1 1.2 5.3z"/></symbol>
    <symbol id="icon-pin" viewBox="0 0 24 24"><path d="M12 1a8 8 0 0 0-8 8c0 6 8 14 8 14s8-8 8-14a8 8 0 0 0-8-8zm0 11a3 3 0 1 1 0-6 3 3 0 0 1 0 6z"/></symbol>
  </defs>
</svg>

<!-- Letterhead -->
<section class="sheet letterhead">
  <div class="wordmark"><span class="name">FENWARDE</span><span class="tag">OUTDOOR ADVERTISING</span></div>
  <svg class="swoosh" width="484" height="692" viewBox="0 0 484 692" aria-hidden="true">
    <path d="M0 648C200 655 400 610 484 546V692H0Z" fill="var(--brand-blue)"/>
    <path d="M0 633Q220 690 484 633V687H0Z" fill="var(--footer-blue)"/>
    <path d="M0 622C160 640 390 610 484 515V528C390 630 160 655 0 637Z" fill="var(--swoosh-black)"/>
    <path d="M0 586C130 620 300 610 381 564C300 622 150 636 0 617Z" fill="var(--swoosh-gray)"/>
  </svg>
  <div class="letterhead-footer">
    <div class="contact phone"><svg><use href="#icon-phone"/></svg><span>512-608-2917</span></div>
    <div class="contact mail"><svg><use href="#icon-mail"/></svg><span>dale@fenwardeoutdoor.example</span></div>
    <div class="contact web"><svg><use href="#icon-globe"/></svg><span>fenwardeoutdoor.example</span></div>
    <div class="contact addr"><svg><use href="#icon-pin"/></svg><span>4857 Mesa Rd. 318 N. PO BOX 582917<br>Austin, TX 78651</span></div>
  </div>
</section>

<!-- Envelope -->
<section class="sheet envelope">
  <div class="envelope-body">
    <svg class="swoosh" width="505" height="252" viewBox="0 0 505 252" aria-hidden="true">
      <path d="M0 232C220 240 420 190 505 131V252H0Z" fill="var(--brand-blue)"/>
      <path d="M0 220C100 230 180 245 220 252H0Z" fill="var(--wedge-blue)"/>
      <path d="M0 209C190 225 420 190 505 101V112C420 200 190 238 0 222Z" fill="var(--swoosh-black)"/>
      <path d="M0 176C120 205 300 195 394 146C300 205 140 215 0 197Z" fill="var(--swoosh-gray)"/>
    </svg>
  </div>
  <svg class="flap" width="505" height="56" viewBox="0 0 505 56" aria-hidden="true">
    <path d="M0 56L8 6Q9 0 15 0H490Q496 0 497 6L505 56Z" fill="var(--brand-blue)"/>
  </svg>
  <div class="wordmark on-blue"><span class="name">FENWARDE</span><span class="tag">OUTDOOR ADVERTISING</span></div>
</section>

<!-- Business card, back -->
<section class="sheet card-back">
  <div class="wordmark on-blue"><span class="name">FENWARDE</span><span class="tag">OUTDOOR ADVERTISING</span></div>
</section>

<!-- Business card, front -->
<section class="sheet card-front">
  <div class="wordmark"><span class="name">FENWARDE</span><span class="tag">OUTDOOR ADVERTISING</span></div>
  <div class="person">
    <div class="person-name">Dale Fenwarde</div>
    <div class="person-role">President</div>
  </div>
  <div class="card-contacts">
    <div class="contact"><svg><use href="#icon-phone"/></svg><span>512-608-2917</span></div>
    <div class="contact"><svg style="color:var(--brand-blue)"><use href="#icon-mail"/></svg><span>dale@fenwardeoutdoor.example</span></div>
    <div class="contact"><svg><use href="#icon-globe"/></svg><span>fenwardeoutdoor.example</span></div>
    <div class="contact"><svg><use href="#icon-pin"/></svg><span>4857 Mesa Rd. 318 N. PO BOX 582917<br>Austin, TX 78651</span></div>
  </div>
</section>

</body>
</html>
```